Marlowe Sail Works President Business Card Carbon fiber catamarans

Hi.. I need a new business card design.. I am the President of a high tech yacht builder. We build Carbon Fiber go fast catamarans... Maybe we use the file I am sharing to you as the back of the card.. We need to look cool and crisp ...

Target Market(s)

Affluent People who will purchase a cool yacht

Industry/Entity Type

Custom Yacht Builder

Contact Information for Business Card

Dean Pellington , President, 512.608.3419 USA

Font styles to use
Serif

Requirements
Must have
• the clean crisp cool feel
Nice to have
• clean and crisp
Should not have
• Bold ugly

```html
<!DOCTYPE html>
<html lang="en">
<head>
<meta charset="utf-8">
<title>Marlowe Sail Works – Business Card</title>
<link href="https://fonts.googleapis.com/css2?family=Michroma&family=Arimo:wght@400&display=swap" rel="stylesheet">
<style>
  :root {
    --backdrop: #878787;
    --card-white: #ffffff;
    --card-black: #000000;
    --ink-dark: #2a2a2a;
    --ink-mid: #3c3c3c;
    --ink-light: #e6e6e6;
    --silver: #c9c9c9;
    --rule-light: #d8d8d8;
    --rule-dark: #8a8a8a;
  }
  * { margin: 0; padding: 0; box-sizing: border-box; }
  html, body { width: 1075px; height: 1200px; overflow: hidden; background: var(--backdrop); }
  .canvas { position: relative; width: 1075px; height: 1200px; }

  .card {
    position: absolute;
    left: 206px;
    width: 663px;
    height: 396px;
    overflow: hidden;
    box-shadow: 2px 3px 3px rgba(0,0,0,0.45);
  }
  .card--front { top: 187px; background: var(--card-white); }
  .card--back { top: 637px; background: var(--card-black); }

  .brand { position: absolute; display: flex; align-items: center; gap: 18px; }
  .brand__mark { width: 62px; height: 62px; border-radius: 50%; border: 3px solid currentColor; flex: none; }
  .brand__name { font-family: "Michroma", sans-serif; font-weight: 400; line-height: 1; }
  .brand__name span { display: block; }
  .brand__line1 { font-size: 31px; letter-spacing: 5px; }
  .brand__line2 { font-size: 18px; letter-spacing: 4.5px; margin-top: 10px; }

  .card--front .brand { left: 275px; top: 80px; color: var(--ink-mid); }
  .card--back .brand { left: 129px; top: 160px; color: var(--silver); }

  .person { position: absolute; left: 38px; top: 213px; }
  .person__name { font-family: "Michroma", sans-serif; font-size: 18px; letter-spacing: 3px; color: var(--ink-dark); }
  .person__title { font-family: "Arimo", sans-serif; font-size: 17px; color: var(--ink-mid); margin-top: 4px; }

  .person-rule {
    position: absolute; left: 35px; top: 272px; width: 250px; height: 6px;
    background: linear-gradient(to bottom, var(--rule-light), var(--rule-dark));
  }

  .contact-band { position: absolute; left: 0; top: 272px; width: 100%; height: 124px; background: var(--card-black); }
  .person-rule { z-index: 2; }

  .contact-list { position: absolute; top: 40px; list-style: none; font-family: "Arimo", sans-serif; font-size: 17px; color: var(--ink-light); }
  .contact-list li { display: flex; align-items: center; gap: 8px; height: 25px; }
  .contact-list--left { left: 37px; }
  .contact-list--right { right: 34px; top: 45px; }
  .contact-list--right li { justify-content: flex-end; }
  .icon { width: 17px; height: 17px; flex: none; fill: var(--ink-light); }
</style>
</head>
<body>
<div class="canvas">

  <section class="card card--front">
    <div class="brand">
      <div class="brand__mark"></div>
      <div class="brand__name"><span class="brand__line1">MARLOWE</span><span class="brand__line2">SAIL WORKS</span></div>
    </div>

    <div class="person">
      <p class="person__name">DEAN PELLINGTON</p>
      <p class="person__title">President</p>
    </div>

    <div class="contact-band">
      <ul class="contact-list contact-list--left">
        <li>
          <svg class="icon" viewBox="0 0 24 24"><path d="M6.6 10.8a15.1 15.1 0 0 0 6.6 6.6l2.2-2.2c.3-.3.7-.4 1-.2 1.1.4 2.3.6 3.6.6.6 0 1 .4 1 1V20c0 .6-.4 1-1 1A17 17 0 0 1 3 4c0-.6.4-1 1-1h3.5c.6 0 1 .4 1 1 0 1.3.2 2.5.6 3.6.1.3 0 .7-.2 1z"/></svg>
          512.608.3419
        </li>
        <li>
          <svg class="icon" viewBox="0 0 24 24"><path d="M2 5h20v14H2zm2 2v.5l8 5 8-5V7zm0 2.8V17h16V9.8l-8 5z"/></svg>
          info@marlowesail.com
        </li>
      </ul>
      <ul class="contact-list contact-list--right">
        <li>
          Texas 78701, USA
          <svg class="icon" viewBox="0 0 24 24"><path d="M12 2a7 7 0 0 0-7 7c0 5.2 7 13 7 13s7-7.8 7-13a7 7 0 0 0-7-7zm0 9.5a2.5 2.5 0 1 1 0-5 2.5 2.5 0 0 1 0 5z"/></svg>
        </li>
        <li>
          www.marlowesailworks.com
          <svg class="icon" viewBox="0 0 24 24"><path d="M12 2a10 10 0 1 0 0 20 10 10 0 0 0 0-20zm6.9 6h-3a15 15 0 0 0-1.3-3.9A8 8 0 0 1 18.9 8zM12 4c.8 1.2 1.5 2.5 1.9 4h-3.8c.4-1.5 1.1-2.8 1.9-4zM4.3 14a8 8 0 0 1 0-4h3.4a16 16 0 0 0 0 4zm.8 2h3a15 15 0 0 0 1.3 3.9A8 8 0 0 1 5.1 16zm3-8h-3a8 8 0 0 1 4.3-3.9A15 15 0 0 0 8.1 8zM12 20c-.8-1.2-1.5-2.5-1.9-4h3.8c-.4 1.5-1.1 2.8-1.9 4zm2.3-6H9.7a14 14 0 0 1 0-4h4.6a14 14 0 0 1 0 4zm.3 5.9a15 15 0 0 0 1.3-3.9h3a8 8 0 0 1-4.3 3.9zm1.7-5.9a16 16 0 0 0 0-4h3.4a8 8 0 0 1 0 4z"/></svg>
        </li>
      </ul>
    </div>
    <div class="person-rule"></div>
  </section>

  <section class="card card--back">
    <div class="brand">
      <div class="brand__mark"></div>
      <div class="brand__name"><span class="brand__line1">MARLOWE</span><span class="brand__line2">SAIL WORKS</span></div>
    </div>
  </section>

</div>
</body>
</html>
```